Redesign Our Presentation on Rational Prescribing

We are looking for a new designer for QVMed, a project that creates educational modules for healthcare providers in the District of Columbia (more information at hlb.example-gov.org/qvmed). We want someone to redesign our powerpoints to look clean and professional, with original graphics that reflect the content on the slides. We also want someone who is creative and could potentially also redesign factsheets, written reports, and promotional postcards.

All the text on the slides must stay the same and it must be in the template (red line at the top, with the red box at the bottom, with the Harlow Bureau of Wellness logo). We want a powerpoint that features original graphics, looks professional, looks clean and is easy to read.

Industry/Entity Type

Healthcare

```html
<!DOCTYPE html>
<html lang="en">
<head>
<meta charset="utf-8">
<title>QVMed – Rational Prescribing Slides</title>
<link href="https://fonts.googleapis.com/css2?family=Roboto:wght@300;400;700&display=swap" rel="stylesheet">
<style>
:root{
  --board:#58595b;
  --paper:#ffffff;
  --navy:#2b2a6e;
  --red:#e8202a;
  --ink:#1f2d4a;
  --band:#e3e3e3;
  --rule:#9a9a9a;
}
*{margin:0;padding:0;box-sizing:border-box}
html,body{width:1200px;height:887px;overflow:hidden;background:var(--board);font-family:"Roboto",Arial,sans-serif;color:var(--ink)}
.canvas{position:relative;width:1200px;height:887px}
.slide{position:absolute;width:553px;height:312px;background:var(--paper);overflow:hidden}
.slide--1{left:20px;top:78px}
.slide--2{left:613px;top:78px}
.slide--3{left:22px;top:450px}
.slide--4{left:614px;top:450px}
.slide__title{position:absolute;left:33px;top:33px;font-weight:400;font-size:14.5px;letter-spacing:.2px;text-transform:uppercase;color:var(--ink)}
.slide__rule{position:absolute;left:35px;right:0;top:60px;height:1.5px;background:var(--red)}
.brand{position:absolute;right:8px;top:12px;width:84px;display:flex;align-items:flex-start;gap:4px;font-weight:700;font-size:9.5px;line-height:1.05;color:var(--navy)}
.brand__mark{flex:none;width:9px;height:9px;background:var(--navy);margin-top:1px}
.slide__footer{position:absolute;left:0;right:0;bottom:0;height:22px;background:var(--red);color:#fff}
.slide__num{position:absolute;left:20px;top:6px;font-size:8px;opacity:.8}
.slide__url{position:absolute;right:26px;top:4px;font-size:11.5px}
.abs{position:absolute}
svg.abs{overflow:visible}
/* slide 1 */
.pyr-lead{left:181px;top:89px;width:330px;font-size:8.8px;line-height:1.3}
.pyr-label{font-size:9px}
.pyr-pct{font-weight:700;font-size:13px;fill:#fff}
.pyr-sym{font-size:10px;fill:#fff}
/* slide 2 */
.adr-item{left:118px;width:380px;font-size:7px;line-height:1.3}
.adr-num{font-size:8px}
/* slide 3 */
.subhead{left:0;width:553px;top:71px;text-align:center;font-size:14.5px}
.stat{font-weight:700;font-size:13px;color:var(--ink)}
.stat-text{font-size:9.5px}
.source{font-weight:700;font-size:11px;text-align:center;line-height:1.15}
.predictors{left:311px;top:187px;width:210px;font-size:9.5px;line-height:1.35}
/* slide 4 */
.step{font-size:8.6px;line-height:1.3}
.step ul{margin-top:3px;padding-left:8px;font-size:7.6px}
.node-num{font-size:9px;fill:#fff}
</style>
</head>
<body>
<main class="canvas">

  <!-- Slide 2 of deck -->
  <section class="slide slide--1">
    <h2 class="slide__title">Consequences of multiple medication use</h2>
    <div class="slide__rule"></div>
    <div class="brand"><span class="brand__mark"></span><span>Harlow Bureau of Wellness</span></div>

    <svg class="abs" style="left:0;top:0" width="553" height="312" viewBox="0 0 553 312">
      <rect x="185" y="130" width="325" height="37" fill="var(--band)"/>
      <rect x="185" y="171" width="325" height="39" fill="var(--band)"/>
      <rect x="185" y="214" width="325" height="42" fill="var(--band)"/>
      <polygon points="140,87 154,127 126,127" fill="var(--navy)"/>
      <polygon points="125,130 155,130 168,167 112,167" fill="var(--red)"/>
      <polygon points="111,170 169,170 183,210 97,210" fill="var(--navy)"/>
      <polygon points="96,213 184,213 200,257 80,257" fill="var(--red)"/>
      <text class="pyr-sym" x="140" y="112" text-anchor="middle">&gt;</text>
      <text class="pyr-pct" x="140" y="153" text-anchor="middle">13%</text>
      <text class="pyr-pct" x="140" y="195" text-anchor="middle">58%</text>
      <text class="pyr-pct" x="140" y="240" text-anchor="middle">82%</text>
      <text class="pyr-label" x="203" y="151" fill="var(--ink)">The risk of ADRs when taking two medicines</text>
      <text class="pyr-label" x="226" y="193" fill="var(--ink)">The risk of ADRs when taking five medicines is</text>
      <text class="pyr-label" x="254" y="231" fill="var(--ink)">The risk of ADRs when taking seven medicines</text>
      <text class="pyr-label" x="254" y="243" fill="var(--ink)">(Dawson 2015)</text>
    </svg>
    <p class="abs pyr-lead">The use of several medications simultaneously, even at otherwise appropriate doses, increases the risk of adverse effects, drug interactions, non-adherence, and death.</p>

    <footer class="slide__footer"><span class="slide__num">2</span><span class="slide__url">www.hlb.example-gov.org</span></footer>
  </section>

  <!-- Slide 3 of deck -->
  <section class="slide slide--2">
    <h2 class="slide__title">Predicting ADRs</h2>
    <div class="slide__rule"></div>
    <div class="brand"><span class="brand__mark"></span><span>Harlow Bureau of Wellness</span></div>

    <svg class="abs" style="left:0;top:0" width="553" height="312" viewBox="0 0 553 312">
      <circle cx="94" cy="102" r="11" fill="none" stroke="var(--navy)" stroke-width="1.3" stroke-dasharray="3 2"/>
      <text class="adr-num" x="94" y="105" text-anchor="middle" fill="var(--navy)">01</text>
      <circle cx="94" cy="166" r="11" fill="none" stroke="var(--red)" stroke-width="1.3" stroke-dasharray="3 2"/>
      <text class="adr-num" x="94" y="169" text-anchor="middle" fill="var(--red)">02</text>
      <circle cx="94" cy="240" r="11" fill="none" stroke="var(--navy)" stroke-width="1.3" stroke-dasharray="3 2"/>
      <text class="adr-num" x="94" y="243" text-anchor="middle" fill="var(--navy)">03</text>
    </svg>
    <p class="abs adr-item" style="top:97px">Few ADRs represent improper prescribing</p>
    <p class="abs adr-item" style="top:147px">Most ADRs are related to the pharmacologic properties of a drug. <b>(For eg.</b> Benzodiazepines cause increased imbalance and gait instability associated with increased risk of falls. A patient taking a nightly benzodiazepine to induce sleep is at high risk for falls. All subsequent health-care costs and associated debility are due to the prescribed medication)</p>
    <p class="abs adr-item" style="top:211px">Many ADRs are both predictable and avoidable (Dawson &amp; Moran 2015) <b>(For eg.</b> Anticholinergic medications prescribed to control bladder spasm may result in constipation and even mental status changes. These are expected outcomes from modulating acetylcholine levels. This type of drug-associated adverse effect raises the risk of prescribing additional medications, such as constipation-relieving agents, to address adverse effects of the original drug. Eliminating, changing, or lowering the dose of the original drug is the right course of action.</p>

    <footer class="slide__footer"><span class="slide__num">3</span><span class="slide__url">www.hlb.example-gov.org</span></footer>
  </section>

  <!-- Slide 4 of deck -->
  <section class="slide slide--3">
    <h2 class="slide__title">Drug classes most commonly involved in ADRs</h2>
    <div class="slide__rule"></div>
    <div class="brand"><span class="brand__mark"></span><span>Harlow Bureau of Wellness</span></div>

    <p class="abs subhead">ADRs during hospitalization</p>
    <svg class="abs" style="left:0;top:0" width="553" height="312" viewBox="0 0 553 312">
      <circle cx="138" cy="207" r="64" fill="var(--navy)"/>
      <circle cx="138" cy="207" r="45" fill="var(--red)"/>
      <circle cx="138" cy="207" r="28" fill="var(--navy)"/>
      <circle cx="138" cy="207" r="10" fill="var(--red)"/>
      <g stroke="var(--rule)" stroke-width="1.3" fill="none">
        <polyline points="138,207 208,112 232,112"/>
        <polyline points="150,220 210,144 232,144"/>
        <polyline points="170,230 215,175 232,175"/>
        <polyline points="182,246 220,200"/>
      </g>
    </svg>
    <span class="abs stat" style="left:232px;top:104px">34%</span>
    <span class="abs stat-text" style="left:307px;top:105px">Cardiovascular agents</span>
    <span class="abs stat" style="left:232px;top:136px">18%</span>
    <span class="abs stat-text" style="left:309px;top:138px">Analgesic medications</span>
    <span class="abs stat" style="left:232px;top:167px">10%</span>
    <span class="abs stat-text" style="left:309px;top:169px">Anti-diabetic drugs</span>
    <span class="abs source" style="left:222px;top:196px;width:70px">Tanabe<br>2012</span>
    <p class="abs predictors">Predictors of ADRs included the number of medications, use of hypoglycaemic agents, history of hyperlipidaemia, raised white cell count on admission and length of stay.</p>

    <footer class="slide__footer"><span class="slide__num">4</span><span class="slide__url">www.hlb.example-gov.org</span></footer>
  </section>

  <!-- Slide 5 of deck -->
  <section class="slide slide--4">
    <h2 class="slide__title">Best drugs in diabetic elders</h2>
    <div class="slide__rule"></div>
    <div class="brand"><span class="brand__mark"></span><span>Harlow Bureau of Wellness</span></div>

    <svg class="abs" style="left:0;top:0" width="553" height="312" viewBox="0 0 553 312">
      <line x1="56" y1="119" x2="510" y2="119" stroke="var(--rule)" stroke-width="1" stroke-dasharray="2 2"/>
      <circle cx="94" cy="119" r="10" fill="var(--navy)"/>
      <text class="node-num" x="94" y="122" text-anchor="middle">01</text>
      <circle cx="221" cy="119" r="10" fill="var(--red)"/>
      <text class="node-num" x="221" y="122" text-anchor="middle">02</text>
      <circle cx="339" cy="119" r="10" fill="var(--navy)"/>
      <text class="node-num" x="339" y="122" text-anchor="middle">03</text>
      <circle cx="461" cy="119" r="10" fill="var(--red)"/>
      <text class="node-num" x="461" y="122" text-anchor="middle">04</text>
    </svg>
    <p class="abs step" style="left:56px;top:164px;width:95px">Only metformin should be used to achieve hemoglobin A1c &lt; 7.5% in most older adults with type 2 diabetes.</p>
    <p class="abs step" style="left:185px;top:190px">Avoid insulin!</p>
    <p class="abs step" style="left:304px;top:148px;width:82px">Insulin-related hypoglycemia and errors are implicated in an estimated 9.2% of ED visits associated with ADE (Gellner et al 2014)</p>
    <div class="abs step" style="left:426px;top:148px;width:108px">
      <p>This one preventable ADE accounts for nearly 100,000 ED Visits every year.</p>
      <ul><li>Patients at or above the age of 80 were twice as likely to visit the ED and 5 times more likely to be hospitalized</li></ul>
    </div>

    <footer class="slide__footer"><span class="slide__num">5</span><span class="slide__url">www.hlb.example-gov.org</span></footer>
  </section>

</main>
</body>
</html>
```